Retail Fitness Store requires Flyer for Women's Mini Marathon

Our retail store will be present as a vendor at a collection point for a women's mini marathon, target audience is 18-40
http://www.larkfieldladiesrun.ie

We need you to design a elegant flyer to be handed out on the day to advertise our fitness store focusing on female products. the following information needs to be shown, business name, address, contact number.

What we do, you can use images or text for the following, mini bands, power bands, rollers, knee sleeves, aerobic bars, vinyl dumbbells, hula hoops, women gloves, weightlifting belts, compression bv sports bras, compression tops / bottoms, ab rollers, pilates, yoga, fitness books.

Also mention we do a large range of other fitness equipment for strength training, olympic lifting, power lifting.

All information can be taking from our website www.quorvafit.com

Target Market(s)

18 - 40 female fitness enthusiats

Industry/Entity Type

Health And Wellness

Font styles to use
Sans Serif

Requirements
Must have
• Quorva Fitness Strore
• 5 & 6 Willowmere Yard
• Tansley Road Dublin
• 00353 1 628 9142
• www.quorvafit.com
Nice to have
• nice colour - a few images -
Should not have
• dark colours - image son men training or heavy weights
• please feel free to change the back ground colour of the logo that has been uploaded.

```html
<!DOCTYPE html>
<html lang="en">
<head>
<meta charset="utf-8">
<title>Quorva Fitness – Ladies Run Flyer</title>
<link rel="stylesheet" href="https://fonts.googleapis.com/css2?family=Anton&family=Lato:wght@400;700&display=swap">
<style>
  :root{
    --sky:#1ba8dd;
    --sky-deep:#0c79b4;
    --ink:#1b1b1b;
    --band:#2a2a2b;
    --cream:#f8e99a;
    --paper:#ffffff;
    --stage:#eceff1;
    --footer:#151515;
    --muted:#d9d9d9;
  }
  *{box-sizing:border-box;margin:0;padding:0}
  html,body{width:1200px;height:1121px;overflow:hidden;background:var(--stage)}
  .flyer{
    position:absolute;left:215px;top:20px;width:909px;height:1275px;
    transform:scale(0.848);transform-origin:top left;
    background:var(--paper);overflow:hidden;
    font-family:"Lato",sans-serif;color:var(--ink);
    box-shadow:0 6px 24px rgba(0,0,0,.18);
  }
  .header{
    position:absolute;left:0;top:0;width:909px;height:172px;
    background:linear-gradient(180deg,var(--sky) 0%,var(--sky-deep) 100%);
    text-align:center;font-family:"Anton",sans-serif;line-height:1;
  }
  .header h1{font-weight:400}
  .header .line-1{display:block;color:var(--ink);font-size:60px;padding-top:26px}
  .header .line-2{display:block;color:#fff;font-size:58px;padding-top:12px}
  .hero-photo{
    position:absolute;left:0;top:186px;width:909px;height:742px;
    background:linear-gradient(160deg,#8fb4c9 0%,#c9d6dc 40%,#c78a6a 62%,#a46a4e 100%);
  }
  .panels{position:absolute;left:0;top:0}
  .section-title{
    position:absolute;left:24px;font-family:"Anton",sans-serif;font-weight:400;
    color:var(--sky);font-size:36px;line-height:1;
  }
  .copy{position:absolute;left:27px;font-size:16px;line-height:20px;text-align:justify}
  .copy p+p{margin-top:8px}
  .about-copy{top:238px;width:430px}
  .services-copy{top:602px;width:480px}
  .product-list{
    position:absolute;top:697px;left:36px;list-style:none;font-size:16px;line-height:25px;
  }
  .product-list.col-2{left:242px;top:699px}
  .product-list li{display:flex;align-items:center;gap:14px}
  .product-list svg{width:11px;height:11px;flex:none}
  .range-note{position:absolute;left:28px;top:872px;width:520px;font-weight:700;font-size:18px;line-height:23px}
  .strip{position:absolute;left:0;top:928px;width:909px;height:177px;background:var(--sky)}
  .strip-art{position:absolute;left:0;top:0}
  .footer{position:absolute;left:0;top:1108px;width:909px;height:167px;background:var(--footer);color:#fff}
  .brand{position:absolute;left:58px;top:52px;font-weight:700;font-size:28px;line-height:34px;color:var(--sky)}
  .brand span{display:block}
  .contact{position:absolute;right:33px;top:18px;text-align:right;font-size:16px;line-height:20px}
  .contact a,.contact .hl{color:var(--sky);text-decoration:none}
  .contact .hours{font-size:14px;margin-bottom:10px}
  .contact .row{display:flex;justify-content:flex-end;gap:64px}
  .contact .gap{margin-top:10px}
</style>
</head>
<body>
<main class="flyer">
  <header class="header">
    <h1><span class="line-1">Join the women's mini marathon</span><span class="line-2">with our fitness equipment</span></h1>
  </header>

  <div class="hero-photo" role="img" aria-label="Photo of a woman in a coral top and grey shorts stretching her leg, holding a pink running shoe, with the sea behind"></div>

  <svg class="panels" width="909" height="928" viewBox="0 0 909 928" aria-hidden="true">
    <rect x="0" y="172" width="909" height="6" fill="#fff"/>
    <rect x="0" y="178" width="909" height="8" fill="var(--band)"/>
    <polygon points="0,186 476,186 484,226 0,226" fill="var(--band)"/>
    <polygon points="0,226 455,226 510,545 0,545" fill="var(--cream)"/>
    <polygon points="0,545 536,545 545,595 0,595" fill="var(--band)"/>
    <polygon points="0,595 515,595 575,928 0,928" fill="var(--cream)"/>
  </svg>

  <h2 class="section-title" style="top:184px">About us</h2>
  <div class="copy about-copy">
    <p>Located in the heart of Dublin, Quorva Fitness is Ireland’s most comprehensive supplier of fitness equipment, apparel, footwear, accessories, nutritional supplements and training materials. We carry the largest selection of premium and top-of-the-line items from trusted brand names as well as a broad variety of budget items that won’t break the bank.</p>
    <p>Our clientele includes everyone from personal trainers, physical therapists, gyms and group fitness or physical educucaton instructors to individuals simply looking to improve their overall fitness.</p>
    <p>Quorva Fitness is an authorised distributor of Harrowby Weightlifting Bars and an official merchant of Strideline Weightlifting Shoes. We offer competitive pricing and shipping throughout the EU.</p>
  </div>

  <h2 class="section-title" style="top:553px">What we do</h2>
  <div class="copy services-copy">
    <p>Items are available individually or sold in bulk. For quotes on goods or shipping, add items to your cart and proceed to checkout. At the bottom of page, select the Estimate button. An estimate of your purchase will be emailed to you within 2 minutes.</p>
  </div>

  <ul class="product-list col-1">
    <li><svg viewBox="0 0 12 12"><path d="M1 6.5l3 3 7-7" fill="none" stroke="var(--sky)" stroke-width="2.2"/></svg>Mini bands,</li>
    <li><svg viewBox="0 0 12 12"><path d="M1 6.5l3 3 7-7" fill="none" stroke="var(--sky)" stroke-width="2.2"/></svg>Power bands</li>
    <li><svg viewBox="0 0 12 12"><path d="M1 6.5l3 3 7-7" fill="none" stroke="var(--sky)" stroke-width="2.2"/></svg>Rollers</li>
    <li><svg viewBox="0 0 12 12"><path d="M1 6.5l3 3 7-7" fill="none" stroke="var(--sky)" stroke-width="2.2"/></svg>Knee sleeves</li>
    <li><svg viewBox="0 0 12 12"><path d="M1 6.5l3 3 7-7" fill="none" stroke="var(--sky)" stroke-width="2.2"/></svg>Aerobic bars</li>
    <li><svg viewBox="0 0 12 12"><path d="M1 6.5l3 3 7-7" fill="none" stroke="var(--sky)" stroke-width="2.2"/></svg>Vinyl dumbbells</li>
    <li><svg viewBox="0 0 12 12"><path d="M1 6.5l3 3 7-7" fill="none" stroke="var(--sky)" stroke-width="2.2"/></svg>Hula hoops</li>
  </ul>
  <ul class="product-list col-2">
    <li><svg viewBox="0 0 12 12"><path d="M1 6.5l3 3 7-7" fill="none" stroke="var(--sky)" stroke-width="2.2"/></svg>Women gloves</li>
    <li><svg viewBox="0 0 12 12"><path d="M1 6.5l3 3 7-7" fill="none" stroke="var(--sky)" stroke-width="2.2"/></svg>Weightlifting belts</li>
    <li><svg viewBox="0 0 12 12"><path d="M1 6.5l3 3 7-7" fill="none" stroke="var(--sky)" stroke-width="2.2"/></svg>Sports bras,</li>
    <li><svg viewBox="0 0 12 12"><path d="M1 6.5l3 3 7-7" fill="none" stroke="var(--sky)" stroke-width="2.2"/></svg>Compression tops / bottoms</li>
    <li><svg viewBox="0 0 12 12"><path d="M1 6.5l3 3 7-7" fill="none" stroke="var(--sky)" stroke-width="2.2"/></svg>Ab rollers</li>
    <li><svg viewBox="0 0 12 12"><path d="M1 6.5l3 3 7-7" fill="none" stroke="var(--sky)" stroke-width="2.2"/></svg>Pilates, yoga, fitness books</li>
  </ul>

  <p class="range-note">We do a large range of other fitness equipment for strength training, olympic lifting, power lifting.</p>

  <section class="strip">
    <svg class="strip-art" width="909" height="177" viewBox="0 0 909 177">
      <rect x="0" y="0" width="909" height="8" fill="var(--sky)"/>
      <polygon points="0,10 255,10 285,160 0,160" fill="#fff"/>
      <polygon points="272,10 590,10 612,160 300,160" fill="#fff"/>
      <polygon points="603,10 890,10 890,160 630,160" fill="#fff"/>
      <rect x="0" y="164" width="909" height="13" fill="#fff"/>
      <rect x="18" y="30" width="215" height="110" fill="var(--muted)" role="img" aria-label="Black hand print and pair of footprints"/>
      <rect x="318" y="30" width="255" height="110" fill="var(--muted)" role="img" aria-label="Black compression top and black rubber floor mat"/>
      <rect x="640" y="25" width="240" height="120" fill="var(--muted)" role="img" aria-label="Orange physiotherapy icon and supplement bottles"/>
    </svg>
  </section>

  <footer class="footer">
    <div class="brand"><span>Quorva</span><span>Fitness Store</span></div>
    <div class="contact">
      <p>Shop online at <a href="#">www.quorvafit.com/store</a></p>
      <p class="gap">or visit our retail location at <span class="hl">Unit 5/6 Willowmere Yard in</span></p>
      <p class="hl">Tansley Road, Dublin 8</p>
      <p class="hours">(Monday through Saturday from 10am – 18.00)</p>
      <div class="row"><p>Email at <a href="#">info@quorvafit.com</a></p><p>Phone on <span class="hl">01 6289142</span></p></div>
    </div>
  </footer>
</main>
</body>
</html>
```